Marijuana Lifestyle Multi-Shop Brand Website

We need a website that provides an online retail shop for our products, along with the additional functionality:

Main Page: Slider with great photography (we are still looking for a professional photographer to take photos for us.

Shop Tab: E-commerce site.
- Main Categories:
- Accessories
- Bubblers
- Dry Pieces
- Scientific Glass
- Water Pipes
- Custom Shop
- University Store

Stores/Resellers: This is a store look-up, so people can enter their zipcode and find our resellers and partners.

Brand Partners: Just a basic filter and page so that we can highlight our partners and why we've selected them.

Contact Us: Basic Form
- Career Page: Basic Page

About Us: Basic Page

Blog:

Search Bar:

Essentially, we want a near exact copy of this website, but with our brand, logo and content. https://corkwillowbins.com/

This site is really really simple, but we like simple.

Our reserved domain address is: www.runbaketend.com

About Us:
We are multi-shop for marijuana-related accessories. We sell quality glass pipes, vaporizers, amazing storage options, dime bags, custom t-shirts and other stuff.

We have a network of resellers that allow us to put in micro-installations into gift shops, convenience stores, tobacco stores, etc. and we are trying to change the overall perception that buying these items should be mainstream and as transparent as going to the Fen or the Walnut Shop.

I've attached a logo that should give you an idea of our color scheme. We don't have our photography yet for the slider
Updates

As an FYI, for the e-commerce part of my website, I already have a license for WP SwiftTill.

Industry/Entity Type

Shop

```html
<!DOCTYPE html>
<html lang="en">
<head>
<meta charset="utf-8">
<title>Hollow Oak – Product 2</title>
<link href="https://fonts.googleapis.com/css2?family=Arimo:wght@400;700&family=Cabin:wght@500&display=swap" rel="stylesheet">
<style>
:root{
  --stage:#000;
  --page:#1c1c1c;
  --topbar:#222;
  --titlebar:#181818;
  --line:#333;
  --text:#ddd;
  --muted:#999;
  --dim:#777;
  --accent:#8aa61e;
  --accent-btn:#7d9b0b;
  --logo:#b8cc7c;
  --logo-disc:#5f8420;
  --notice:#dff0b6;
  --notice-btn:#b5c39b;
  --scroll:#e6e6e6;
}
*{box-sizing:border-box;margin:0;padding:0}
html,body{width:1200px;height:1000px;overflow:hidden;background:var(--stage);font-family:Arimo,Arial,sans-serif}
.site{position:absolute;left:0;top:163px;width:1200px;height:677px;background:var(--page);overflow:hidden}
.abs{position:absolute}
.scrollbar{right:0;top:0;width:10px;height:677px;background:var(--scroll)}
.topbar{left:0;top:0;width:1190px;height:23px;background:var(--topbar);border-bottom:1px solid #2c2c2c}
.social{left:200px;top:0;display:flex}
.social span{width:23px;height:23px;border-right:1px solid #333;display:flex;align-items:center;justify-content:center}
.social span:first-child{border-left:1px solid #333}
.social i{width:7px;height:7px;border-radius:50%;background:#777}
.utility{left:466px;top:8px;font-size:8px;font-weight:700;color:#aaa;display:flex;white-space:nowrap}
.utility a{color:#aaa;text-decoration:none;padding:0 8px;border-right:1px solid #555;line-height:9px}
.utility a:first-child{padding-left:0}
.utility .contact{padding-left:8px}
.header{left:0;top:23px;width:1190px;height:88px;border-bottom:1px solid #2a2a2a}
.brand{left:212px;top:9px;display:flex;align-items:center;gap:10px}
.brand .disc{width:60px;height:60px;border-radius:50%;background:var(--logo-disc)}
.brand .name{font-size:27px;font-weight:400;color:var(--logo);line-height:1}
.mainnav a{position:absolute;top:39px;font-size:10px;line-height:12px;color:var(--muted);text-decoration:none;white-space:nowrap}
.search{left:971px;top:39px}
.cartbtn{left:1156px;top:26px;width:34px;height:37px;border:1px solid #333;border-right:none;border-bottom:none;display:flex;align-items:center;justify-content:center;background:var(--page)}
.titlebar{left:0;top:111px;width:1190px;height:43px;background:var(--titlebar);border-bottom:1px solid #2a2a2a}
.titlebar h1{position:absolute;left:207px;top:15px;font-size:12px;font-weight:400;color:#fff}
.crumbs{position:absolute;left:791px;top:17px;font-size:8px;color:#ccc;white-space:nowrap}
.notice{left:207px;top:192px;width:778px;height:63px;background:var(--notice)}
.notice p{position:absolute;left:27px;top:26px;font-size:10px;color:#555}
.notice .btn{position:absolute;left:601px;top:18px;width:155px;height:31px;background:var(--notice-btn);color:#fff;font-size:9px;display:flex;align-items:center;justify-content:center}
.mainimg{left:207px;top:294px;width:233px;height:232px;border:1px solid #3a3a3a;padding:4px}
.ph{width:100%;height:100%;background:linear-gradient(#9c9c9c,#6f6f6f)}
.thumb{width:76px;height:76px;border:1px solid #3a3a3a;padding:3px}
.thumb .ph{background:linear-gradient(#a5a5a5,#707070)}
.product{left:478px;top:293px;width:505px}
.product h2{font-family:Cabin,Arial,sans-serif;font-weight:500;font-size:26px;color:#fff;line-height:30px}
.rating{display:flex;align-items:center;gap:6px;font-size:8px;color:#aaa;margin-top:-2px}
.price{color:var(--accent);font-size:11px;margin-top:17px}
.lead{color:var(--text);font-size:10px;margin-top:13px}
.stock{color:var(--accent);font-size:9px;margin-top:14px}
.buy{display:flex;align-items:center;margin-top:9px}
.qty{display:flex;border:1px solid #444;height:31px}
.qty span{width:32px;display:flex;align-items:center;justify-content:center;color:#ddd;font-size:10px}
.qty .step{background:linear-gradient(#333,#111)}
.qty .val{border-left:1px solid #444;border-right:1px solid #444;background:#1a1a1a}
.addcart{margin-left:15px;width:83px;height:31px;background:var(--accent-btn);color:#fff;font-size:9px;display:flex;align-items:center;justify-content:center}
.meta{font-size:8px;color:#999;margin-top:25px}
.meta b{font-weight:400;color:var(--accent)}
.tabs{left:478px;top:528px;display:flex}
.tabs span{height:30px;border:1px solid #3a3a3a;border-left:none;font-size:8px;color:#999;padding:0 9px;display:flex;align-items:center;background:#1f1f1f}
.tabs span:first-child{border-left:1px solid #3a3a3a;font-weight:700;color:#ddd;background:var(--page);border-bottom-color:var(--page)}
.panel{left:478px;top:557px;width:504px;height:140px;border:1px solid #3a3a3a;padding:11px 11px}
.panel h3{font-size:13px;color:#fff;margin-bottom:7px}
.panel p{font-size:10px;line-height:16px;color:var(--text);margin-bottom:8px}
.sidearrow{top:297px;width:21px;height:83px;background:#222;display:flex;align-items:center;justify-content:center}
.minicart{left:975px;top:91px;width:210px;height:228px;background:#1e1e1e;border:1px solid #3a3a3a}
.mc-item{position:relative;height:57px;border-bottom:1px solid #333}
.mc-item b{position:absolute;left:8px;top:9px;font-size:9px;color:#fff}
.mc-item small{position:absolute;left:8px;top:24px;font-size:7px;color:#999}
.mc-item .ph{position:absolute;left:158px;top:8px;width:41px;height:40px;border:2px solid #888;background:linear-gradient(#aaa,#777)}
.subtotal{height:30px;border-bottom:1px solid #333;font-size:9px;color:#aaa;padding:10px 8px}
.subtotal b{color:var(--accent)}
.mc-actions{display:flex;font-size:9px;color:#eee}
.mc-actions span{flex:1;text-align:center;padding-top:8px}
</style>
</head>
<body>
<div class="site">
  <div class="abs scrollbar"></div>

  <div class="abs topbar">
    <div class="abs social"><span><i></i></span><span><i></i></span><span><i></i></span><span><i></i></span><span><i></i></span><span><i></i></span></div>
    <nav class="abs utility"><a>HOME</a><a>About Us</a><a>My Account</a><a>Shop</a><a>Career Page</a><a>Blog</a><a>Contact Us</a><span class="contact">+1 800 555 0142 / info@runbaketend.com</span></nav>
  </div>

  <header class="abs header">
    <div class="abs brand"><span class="disc"></span><span class="name">Hollow Oak</span></div>
    <nav class="mainnav">
      <a style="left:567px">HOME</a>
      <a style="left:616px">About Us</a>
      <a style="left:676px">My Account</a>
      <a style="left:748px">Shop</a>
      <a style="left:790px">Career Page</a>
      <a style="left:864px">Blog</a>
      <a style="left:903px">Contact Us</a>
    </nav>
    <svg class="abs search" width="11" height="11" viewBox="0 0 11 11"><circle cx="4.5" cy="4.5" r="3.3" fill="none" stroke="#999" stroke-width="1.4"/><line x1="7" y1="7" x2="10" y2="10" stroke="#999" stroke-width="1.6"/></svg>
    <div class="abs cartbtn"><svg width="12" height="11" viewBox="0 0 12 11"><path d="M0 1h2l2 6h6l1.5-4.5H3" fill="none" stroke="#fff" stroke-width="1.4"/><circle cx="5" cy="9.5" r="1.1" fill="#fff"/><circle cx="9" cy="9.5" r="1.1" fill="#fff"/></svg></div>
  </header>

  <div class="abs titlebar">
    <h1>Shop</h1>
    <div class="crumbs">You are here: &nbsp;Home &nbsp;/ Shop &nbsp;/ Bubblers &nbsp;/ Product 2</div>
  </div>

  <div class="abs notice"><p>"Product 2" was successfully added to your cart.</p><span class="btn">View Cart</span></div>

  <div class="abs mainimg"><div class="ph" role="img" aria-label="Product photo: two yellow takeaway cups on a grey backdrop"></div></div>
  <div class="abs thumb" style="left:207px;top:541px"><div class="ph" role="img" aria-label="Thumbnail: green cup"></div></div>
  <div class="abs thumb" style="left:286px;top:541px"><div class="ph" role="img" aria-label="Thumbnail: row of yellow cups"></div></div>
  <div class="abs thumb" style="left:365px;top:541px"><div class="ph" role="img" aria-label="Thumbnail: blue cups"></div></div>
  <div class="abs thumb" style="left:207px;top:621px"><div class="ph" role="img" aria-label="Thumbnail: yellow cups"></div></div>

  <section class="abs product">
    <h2>Product 2</h2>
    <div class="rating">
      <svg width="58" height="10" viewBox="0 0 58 10">
        <g fill="#f2c200"><path id="st" d="M5 0l1.5 3.3 3.5.4-2.6 2.4.7 3.5L5 7.9 1.9 9.6l.7-3.5L0 3.7l3.5-.4z"/><use href="#st" x="11.5"/><use href="#st" x="23"/><use href="#st" x="34.5"/></g>
        <use href="#st" x="46" fill="#aaa"/>
      </svg>
      <span>(1 customer review)</span>
    </div>
    <div class="price">$99.99</div>
    <p class="lead">Lorem ipsum dolor sit amet, consectetur adipiscing elit. Donec venenatis tincidunt sem id volutpat.</p>
    <div class="stock">100 in stock (backorders allowed)</div>
    <div class="buy"><div class="qty"><span class="step">-</span><span class="val">1</span><span class="step">+</span></div><span class="addcart">Add to cart</span></div>
    <div class="meta">SKU: HBG002. Category: <b>Bubblers</b>.</div>
  </section>

  <div class="abs tabs"><span>Description</span><span>Additional Information</span><span>Reviews (1)</span></div>
  <div class="abs panel">
    <h3>Product Description</h3>
    <p>Lorem ipsum dolor sit amet, consectetur adipiscing elit. Donec venenatis tincidunt sem id volutpat. Vivamus consectetur pharetra venenatis. Aliquam commodo velit tortor, vel sagittis justo aliquet in. Integer non imperdiet orci, volutpat iaculis dolor.</p>
    <p>Donec quam augue, gravida quis erat at, dignissim tincidunt lectus. Lorem ipsum dolor sit amet, consectetur adipiscing elit. Aenean a commodo nunc. Maecenas et augue purus.</p>
  </div>

  <div class="abs sidearrow" style="left:0"><svg width="6" height="10" viewBox="0 0 6 10"><path d="M5 1L1 5l4 4" fill="none" stroke="#fff" stroke-width="1.5"/></svg></div>
  <div class="abs sidearrow" style="left:1168px"><svg width="6" height="10" viewBox="0 0 6 10"><path d="M1 1l4 4-4 4" fill="none" stroke="#fff" stroke-width="1.5"/></svg></div>

  <aside class="abs minicart">
    <div class="mc-item"><b>Product 1</b><small>2 × $50.00</small><span class="ph" role="img" aria-label="Green cup"></span></div>
    <div class="mc-item"><b>Product 3</b><small>1 × $149.99</small><span class="ph" role="img" aria-label="Blue cups"></span></div>
    <div class="mc-item"><b>Product 2</b><small>1 × $99.99</small><span class="ph" role="img" aria-label="Yellow cups"></span></div>
    <div class="subtotal"><b>Subtotal:</b> $349.98</div>
    <div class="mc-actions"><span>View Cart</span><span>Checkout</span></div>
  </aside>
</div>
</body>
</html>
```